Shipping cards

Expedited delivery of various business related products , packages ,parcels etc. Intrastate or Interstate.

Target Market(s)

business and or private customer base.with expedited needs and short term or long term needs.

Industry/Entity Type

Business

Contact Information for Business Card

would like the silhouette of my dog between the business name Amber{ } Fox . Amber Fox Freight ,Expedited Delivery, tel330-958-3637 fax TBD , dispatch@quillmail.test, Dennis J. Holt- Owner

Font styles to use
Serif

Requirements
Must have
• dog silhouette between Amber Fox or before and after name of company.
Should not have
• remove oval from silhouette around dog

```html
<!DOCTYPE html>
<html lang="en">
<head>
<meta charset="utf-8">
<title>Amber Fox Freight – Business Card</title>
<link rel="stylesheet" href="https://fonts.googleapis.com/css2?family=Crimson+Pro:wght@500;600&family=Open+Sans:wght@400&display=swap">
<style>
  :root {
    --backdrop: #e4e5e7;
    --card: #ffffff;
    --card-edge: #5a5a5a;
    --ink: #111111;
    --brand-red: #b51f22;
    --icon-red: #b3282b;
  }
  html, body {
    margin: 0;
    width: 1200px;
    height: 1200px;
    overflow: hidden;
    background: var(--backdrop);
  }
  .card {
    position: absolute;
    left: 50px;
    top: 287px;
    width: 1100px;
    height: 626px;
    background: var(--card);
    box-shadow: inset 0 0 0 1px var(--card-edge);
    overflow: hidden;
  }
  .card__bands {
    position: absolute;
    inset: 0;
    width: 1100px;
    height: 626px;
  }
  .brand__mark {
    position: absolute;
    left: 111px;
    top: 48px;
    width: 70px;
    height: 70px;
    border-radius: 50%;
    background: var(--ink);
  }
  .brand__name {
    position: absolute;
    left: 223px;
    top: 78px;
    margin: 0;
    font: 600 47px/1 "Crimson Pro", serif;
    color: var(--ink);
  }
  .brand__tagline {
    position: absolute;
    left: 71px;
    top: 132px;
    margin: 0;
    font: 500 28px/1 "Crimson Pro", serif;
    color: var(--brand-red);
  }
  .person {
    position: absolute;
    left: 0;
    right: 0;
    text-align: center;
    margin: 0;
    color: var(--ink);
  }
  .person__name {
    top: 276px;
    font: 600 31px/1 "Crimson Pro", serif;
  }
  .person__role {
    top: 313px;
    font: 400 20px/1 "Open Sans", sans-serif;
  }
  .contact {
    position: absolute;
    left: 0;
    right: 0;
    top: 356px;
    display: flex;
    justify-content: center;
    align-items: center;
    gap: 10px;
    font: 400 22px/1 "Open Sans", sans-serif;
    color: var(--ink);
  }
  .contact__item {
    display: flex;
    align-items: center;
    gap: 7px;
  }
  .contact__icon {
    width: 24px;
    height: 22px;
    fill: var(--icon-red);
  }
</style>
</head>
<body>
  <main class="card">
    <svg class="card__bands" viewBox="0 0 794 452" preserveAspectRatio="none" aria-hidden="true">
      <defs>
        <linearGradient id="band-dark" x1="0" x2="1">
          <stop offset="0" stop-color="#000"/>
          <stop offset="1" stop-color="#3a3a3a"/>
        </linearGradient>
        <linearGradient id="band-grey" x1="0" x2="1">
          <stop offset="0" stop-color="#76777c"/>
          <stop offset="1" stop-color="#e2e2e4"/>
        </linearGradient>
        <linearGradient id="band-red" x1="0" x2="1">
          <stop offset="0" stop-color="#ae1a1c"/>
          <stop offset="0.5" stop-color="#d4765c"/>
          <stop offset="1" stop-color="#f1cdbf"/>
        </linearGradient>
        <linearGradient id="fade-grey" x1="0" x2="1">
          <stop offset="0" stop-color="#ececed"/>
          <stop offset="1" stop-color="#fff"/>
        </linearGradient>
        <linearGradient id="fade-red" x1="0" x2="1">
          <stop offset="0" stop-color="#f8e3da"/>
          <stop offset="1" stop-color="#fff"/>
        </linearGradient>
      </defs>
      <g class="band band--top">
        <polygon points="0,87 52,87 46,119 0,119" fill="url(#band-dark)"/>
        <polygon points="332,87 621,87 615,119 326,119" fill="url(#band-grey)"/>
        <polygon points="633,87 665,87 659,119 627,119" fill="#cfcfd2"/>
        <polygon points="676,87 708,87 702,119 670,119" fill="#d9d9db"/>
        <polygon points="719,87 751,87 745,119 713,119" fill="#e2e2e4"/>
        <polygon points="762,87 794,87 794,119 756,119" fill="url(#fade-grey)"/>
      </g>
      <g class="band band--bottom">
        <polygon points="0,419 626,419 620,452 0,452" fill="url(#band-red)"/>
        <polygon points="638,419 670,419 664,452 632,452" fill="#e5ad97"/>
        <polygon points="681,419 713,419 707,452 675,452" fill="#ebbca9"/>
        <polygon points="724,419 756,419 750,452 718,452" fill="#f1d0c3"/>
        <polygon points="767,419 794,419 794,452 761,452" fill="url(#fade-red)"/>
      </g>
    </svg>

    <header class="brand">
      <span class="brand__mark" aria-hidden="true"></span>
      <h1 class="brand__name">Amber Fox</h1>
      <p class="brand__tagline">Shipping, Expedited Delivery</p>
    </header>

    <p class="person person__name">Dennis J. Holt</p>
    <p class="person person__role">Owner</p>

    <div class="contact">
      <span class="contact__item">
        <svg class="contact__icon" viewBox="0 0 24 22" aria-label="Phone"><path d="M5 2c1-1 2-1 3 0l2 3c.6 1 .3 2-.5 2.6L8 8.6c1 2.3 2.8 4.2 5 5.4l1.1-1.5c.6-.8 1.7-1 2.6-.4l3 2c1 .7 1 1.8.2 2.7l-1.5 1.6c-1.2 1.2-3 1.4-4.5.7C8 16.6 4.5 13 2.5 8 1.9 6.5 2.3 4.8 3.4 3.7z"/></svg>
        412-573-2916
      </span>
      <span class="contact__item">
        <svg class="contact__icon" viewBox="0 0 24 22" aria-label="Fax"><path d="M7 1h8l3 3v5H7zM3 9h18a2 2 0 0 1 2 2v8a2 2 0 0 1-2 2H3a2 2 0 0 1-2-2v-8a2 2 0 0 1 2-2zm2 3v2h14v-2zm0 4v2h3v-2zm5 0v2h3v-2zm5 0v2h3v-2z"/></svg>
        TBD
      </span>
      <span class="contact__item">
        <svg class="contact__icon" viewBox="0 0 24 22" aria-label="Email"><path d="M1 4h22v1.5L12 13 1 5.5zM1 8l11 7.5L23 8v10H1z"/></svg>
        dispatch@quillmail.test
      </span>
    </div>
  </main>
</body>
</html>
```